Speech Pathology card for parents of young children

I need a professional, yet fun card for my speech and language pathology services.
I'm trying to offer my speech therapy services to parents of young children. These parents will most likely be women. I want the card to have a fun feel to it and have a concept of speech and language in it (kind of like the cartoon I've attached below showing a boy/girl talking).

I'd want a white background on the card and to bring in some bright colors as well.

Please include the NOVRE logo in a smaller size on a free corner of the card.

Target Market(s)

parents of young children

Contact Information for Business Card

must have my information and I'd like it to have the NOVRE logo (small) somewhere in the corner)

Font styles to use
Serif
Sans Serif

Colors

Designer to choose colors to be used in the design.

Requirements
Must have
• The card title should read: Speech-Language Pathologist
• Lorena Tuvell
• MS CCC-SLP/TSSLD (this under the name)
• 555 014 2786
• lorentuvell@quillpost.net
Nice to have
• i'm looking for a card with a white background and a fun icon that encompasses speaking... similar to the one I've attached.

```html
<!DOCTYPE html>
<html lang="en">
<head>
<meta charset="utf-8">
<title>Lorena Tuvell – Speech-Language Pathologist</title>
<link rel="stylesheet" href="https://fonts.googleapis.com/css2?family=Amatic+SC:wght@400;700&family=Cormorant+SC:wght@600&display=swap">
<style>
  :root {
    --page: #e4e4e4;
    --card: #ffffff;
    --ink: #2b2b2b;
    --name-blue: #2aa3df;
    --title-red: #e5382f;
    --accent-orange: #f39a1e;
    --bubble-shadow: #d9d9d9;
    --figure-tone-a: #f3c9a8;
    --figure-tone-b: #7cc3e0;
  }
  html, body {
    margin: 0;
    width: 1200px;
    height: 1006px;
    overflow: hidden;
    background: var(--page);
  }
  .business-card {
    position: absolute;
    left: 75px;
    top: 203px;
    width: 1050px;
    height: 600px;
    background: var(--card);
    box-shadow: 0 6px 24px rgba(0,0,0,0.18);
  }
  .speaker-illustration {
    position: absolute;
    left: 110px;
    top: 250px;
    width: 310px;
    height: 290px;
    border-radius: 40px;
    background: linear-gradient(160deg, var(--figure-tone-a) 0%, var(--figure-tone-b) 70%, #e36a5a 100%);
    opacity: 0.55;
  }
  .speech-bubble {
    position: absolute;
    left: 0;
    top: 0;
    width: 1050px;
    height: 600px;
  }
  .bubble-text {
    position: absolute;
    left: 490px;
    top: 120px;
    font-family: "Amatic SC", cursive;
    color: var(--ink);
  }
  .practitioner-name {
    margin: 0;
    font-size: 42px;
    font-weight: 700;
    color: var(--name-blue);
    letter-spacing: 1px;
    line-height: 1;
  }
  .credentials {
    margin: 4px 0 0;
    font-size: 30px;
    font-weight: 700;
    line-height: 1;
  }
  .card-title {
    margin: 34px 0 0;
    font-size: 38px;
    font-weight: 700;
    color: var(--title-red);
    line-height: 1;
  }
  .contact-list {
    list-style: none;
    margin: 34px 0 0;
    padding: 0;
    font-size: 30px;
    font-weight: 700;
    line-height: 1.2;
  }
  .contact-list li {
    display: flex;
    align-items: center;
    gap: 10px;
  }
  .contact-icon {
    width: 22px;
    height: 22px;
    flex: none;
  }
  .association-mark {
    position: absolute;
    right: 80px;
    bottom: 70px;
    display: flex;
    align-items: center;
    gap: 14px;
    font-family: "Cormorant SC", serif;
    font-weight: 600;
    font-size: 34px;
    color: var(--ink);
  }
  .association-dot {
    width: 56px;
    height: 56px;
    border-radius: 50%;
    background: var(--ink);
  }
</style>
</head>
<body>
  <main class="business-card">
    <div class="speaker-illustration" role="img" aria-label="Cartoon illustration of a cheerful child speaking through a megaphone"></div>

    <svg class="speech-bubble" viewBox="0 0 1050 600" aria-hidden="true">
      <path d="M452 330 C420 230 470 110 640 80 C800 55 930 110 945 230 C960 350 820 425 640 420 C560 418 500 400 470 372 L452 338 Z"
            fill="var(--bubble-shadow)" transform="translate(12 10)"/>
      <path d="M452 330 C420 230 470 110 640 80 C800 55 930 110 945 230 C960 350 820 425 640 420 C560 418 500 400 470 372 L452 338 Z"
            fill="#fff" stroke="var(--ink)" stroke-width="2.5" stroke-linejoin="round"/>
    </svg>

    <div class="bubble-text">
      <h1 class="practitioner-name">Lorena Tuvell</h1>
      <p class="credentials">MS CCC-SLP/TSSLD</p>
      <h2 class="card-title">Speech-Language Pathologist</h2>
      <ul class="contact-list">
        <li>
          <svg class="contact-icon" viewBox="0 0 24 24"><path d="M6.6 10.8a15 15 0 0 0 6.6 6.6l2.2-2.2c.3-.3.7-.4 1-.2 1.1.4 2.3.6 3.6.6.6 0 1 .4 1 1V20c0 .6-.4 1-1 1A17 17 0 0 1 3 4c0-.6.4-1 1-1h3.5c.6 0 1 .4 1 1 0 1.3.2 2.5.6 3.6.1.3 0 .7-.2 1z" fill="var(--accent-orange)"/></svg>
          <span>555 014 2786</span>
        </li>
        <li>
          <svg class="contact-icon" viewBox="0 0 24 24"><rect x="2" y="5" width="20" height="14" fill="none" stroke="var(--accent-orange)" stroke-width="2.2"/><path d="M2 5l10 8 10-8" fill="none" stroke="var(--accent-orange)" stroke-width="2.2"/></svg>
          <span>lorentuvell@quillpost.net</span>
        </li>
      </ul>
    </div>

    <div class="association-mark">
      <span class="association-dot"></span>
      <span class="association-name">NOVRE</span>
    </div>
  </main>
</body>
</html>
```